Signage for Brightwell Academy - Exterior

Size 32 ft x 5 ft 11 inches. It will be installed at a height of 25 feet. Should contain the Logo, Address, some courses to give an idea about what we do. The signage is installed on the 2nd floor, so the minimum size of letters would be as in the old signage design attached. The font size of the bottom line of our existing signage is as small as we should go. Basically it should be such that the first glance gives us an idea that it is a Brightwell Academy. You are allowed to change the logo colors, but the font and design will remain the same.
Updates

Reason: some extra time might be needed to improve the designs and get new inputs. need some out of the box designing.

Target Market(s)

High School and College going teens who wish to learn software skills for graphics and animation

Industry/Entity Type

Education

Font styles to use
Other font styles liked:
• Utopia

Colors

Designer to choose colors to be used in the design.

Requirements
Must have
• Logo, Address, Phone Number, website address, what we do.
• 1. Please refer to the image of our old signage uploaded. The font size of the courses mentioned at the bottom of the signage "ANIMATION, GAMING.." is the smallest size which is legible from the ground level.
• 2. We would like at least the web address in legible font size and if possible the phone number too. The physical address could be a little smaller as in the old signage, as that is not a calling factor and in case someone is interested, they can walk closer and read the address.
• 3. The calling factors would be a few courses and some graphics depicting what we do in the first look.
• 4.You are allowed to change the logo colors, but the font and design will remain the same. Prefer usage of Ubuntu font for text.
• 5. Prefer minimalist look and not cluttered. I feel mentioning more courses is making the signage cluttered. we can limit it to 3 courses.
Nice to have
• Graphics to suggest what we do. It should be eye catching. The graphic should be such that speaks of what we do. It should be suggestive.
Should not have
• It should not be too busy

```html
<!DOCTYPE html>
<html lang="en">
<head>
<meta charset="utf-8">
<title>Brightwell Academy – Exterior Signage</title>
<link href="https://fonts.googleapis.com/css2?family=Tinos:wght@400&family=Ubuntu:wght@400;500&display=swap" rel="stylesheet">
<style>
  :root {
    --page: #e9edf2;
    --navy: #182d5a;
    --navy-deep: #10224a;
    --sky: #8fd6ef;
    --white: #ffffff;
    --soft: #cfe0f2;
    --teal: #1aa3b8;
    --cyan: #4cc3e6;
    --lime: #a6cf3a;
    --border: #dfe8f3;
  }
  * { margin: 0; padding: 0; box-sizing: border-box; }
  html, body {
    width: 1200px; height: 800px; overflow: hidden;
    background: var(--page);
  }
  .sign {
    position: absolute; left: 40px; top: 308px;
    width: 1120px; height: 184px;
    background: linear-gradient(90deg, var(--navy-deep) 0%, var(--navy) 55%, var(--navy-deep) 100%);
    border: 3px solid var(--border);
    overflow: hidden;
    color: var(--white);
  }
  .brand {
    position: absolute; left: 22px; top: 30px; width: 300px;
    font-family: "Ubuntu", sans-serif; font-weight: 500;
    color: var(--sky); line-height: 1;
  }
  .brand__name { display: block; font-size: 44px; letter-spacing: 1px; }
  .brand__sub {
    display: block; margin-top: 50px; padding-bottom: 6px;
    font-size: 22px; letter-spacing: 2px;
    border-bottom: 2px solid var(--soft);
  }
  .courses {
    position: absolute; left: 346px; top: 3px;
    list-style: none;
    font-family: "Tinos", serif; font-size: 32px; line-height: 46px;
    letter-spacing: 1px;
  }
  .courses li { display: flex; align-items: center; gap: 14px; }
  .courses svg { width: 24px; height: 24px; flex: none; }
  .website {
    position: absolute; left: 380px; top: 134px;
    font-family: "Tinos", serif; font-size: 42px; line-height: 1;
    letter-spacing: 1px; white-space: nowrap;
  }
  .contact {
    position: absolute; left: 638px; top: 8px; width: 240px;
    font-family: "Tinos", serif; color: var(--soft);
  }
  .contact__pin { display: block; width: 20px; height: 20px; margin-left: 60px; }
  .contact__city { font-size: 21px; letter-spacing: 1px; margin-top: 2px; color: var(--white); line-height: 1.2; }
  .contact__address { font-size: 14px; line-height: 17px; margin-top: 3px; }
  .contact__phone { font-size: 23px; margin-top: 3px; color: var(--white); line-height: 1.2; }
  .graphic {
    position: absolute; right: 0; top: 0;
    width: 200px; height: 100%;
    background: linear-gradient(135deg, var(--lime) 0%, var(--cyan) 45%, var(--teal) 100%);
    clip-path: polygon(35% 0, 100% 0, 100% 100%, 50% 100%, 0 55%);
    opacity: 0.9;
  }
</style>
</head>
<body>
  <div class="sign">
    <div class="brand">
      <span class="brand__name">BRIGHTWELL</span>
      <span class="brand__sub">ACADEMY</span>
    </div>

    <ul class="courses">
      <li><svg viewBox="0 0 24 24"><rect x="2" y="2" width="20" height="20" fill="none" stroke="#fff" stroke-width="2"/><path d="M6 12l4 4 8-9" fill="none" stroke="#fff" stroke-width="2.5"/></svg>VFX</li>
      <li><svg viewBox="0 0 24 24"><rect x="2" y="2" width="20" height="20" fill="none" stroke="#fff" stroke-width="2"/><path d="M6 12l4 4 8-9" fill="none" stroke="#fff" stroke-width="2.5"/></svg>ANIMATION</li>
      <li><svg viewBox="0 0 24 24"><rect x="2" y="2" width="20" height="20" fill="none" stroke="#fff" stroke-width="2"/><path d="M6 12l4 4 8-9" fill="none" stroke="#fff" stroke-width="2.5"/></svg>GRAPHICS</li>
    </ul>

    <div class="website">www.brightwellacademy.in</div>

    <div class="contact">
      <svg class="contact__pin" viewBox="0 0 24 24"><path d="M12 2a7 7 0 0 0-7 7c0 5 7 13 7 13s7-8 7-13a7 7 0 0 0-7-7z" fill="none" stroke="#cfe0f2" stroke-width="2"/><circle cx="12" cy="9" r="2.5" fill="#cfe0f2"/></svg>
      <p class="contact__city">CHANDIGARH</p>
      <p class="contact__address">Sco 12-14, First Floor,<br>Sector 21 B</p>
      <p class="contact__phone">P: 0172 555 0134</p>
    </div>

    <div class="graphic" role="img" aria-label="Decorative cluster of overlapping teal, blue and lime squares and diamonds"></div>
  </div>
</body>
</html>
```